Velstrom Personal Training- Mind, Body, Power

My personal training services incorporates 3 key elements
Mind- setting up a mindset for clients to get real results and continued motivation
Body- Incorporates the physical training aspect of the personal training
Power- Power from good nutrition and supplementation.

These three elements incorporate a truly whole service of personal training and I would like stationery and a logo to represent that.

Velstrom stands for Pyramid which I liken to the persons transformation of their body. A pyramid has a strong base, and is built up over time and a physical transformation takes a really good base and a lot of time to develop.

Also note that the Pyramid usually can be conceptually designed as a triangle.

The winning designer should incorporate the above in a smart way.

PLEASE INCLUDE THE FOLLOWING STATIONERY DESIGNS IN YOUR CONCEPT (not limited to)
- Display folder
- Flyer template
- Brochure template
- Letterhead
- Email Signature

Some examples of work that I really like

http://www.quorvint.example/

Although I do like the same scheme as the link I provided in the brief, please do try and be a bit original with your stationery designs.

Cheers

Target Market(s)

Target market is for business professionals that do not have time or money to work out a training and eating regime

Industry/Entity Type

Nutrition

Requirements
Must have
• Must include a concept of 3 points and or 3 key aspects being mind, body and power.
Should not have
• Any tacky headlines or irrelevant logos

```html
<!DOCTYPE html>
<html lang="en">
<head>
<meta charset="utf-8">
<title>Velstrom Personal Training — Brochure Cover</title>
<link href="https://fonts.googleapis.com/css2?family=Cabin:wght@400;700&display=swap" rel="stylesheet">
<style>
  :root {
    --sand: #ecd79f;
    --charcoal: #2a2a2a;
    --figure: #0e0e0e;
    --band-dark: #241d17;
    --band-mid: #3a3029;
    --cream: #ecd9a0;
    --stone: #a7a7a7;
    --ink: #111111;
  }
  * { margin: 0; padding: 0; box-sizing: border-box; }
  html, body {
    width: 1200px;
    height: 2313px;
    overflow: hidden;
    background: #ffffff;
  }
  .brochure-cover {
    position: relative;
    width: 1200px;
    height: 2313px;
    font-family: "Cabin", sans-serif;
    overflow: hidden;
  }
  .hero {
    position: absolute;
    left: 0; top: 0;
    width: 1200px;
    height: 1260px;
  }
  .hero svg { display: block; }
  .title-band {
    position: absolute;
    left: 0; top: 1260px;
    width: 1200px;
    height: 360px;
    background: linear-gradient(180deg, var(--band-mid) 0%, var(--band-dark) 45%, var(--band-mid) 100%);
    display: flex;
    align-items: center;
  }
  .title-band__text {
    margin-left: 110px;
    color: var(--cream);
    font-size: 104px;
    font-weight: 400;
    letter-spacing: 1px;
    white-space: nowrap;
  }
  .footer-panel {
    position: absolute;
    left: 0; top: 1620px;
    width: 1200px;
    height: 693px;
    background: var(--stone);
    display: flex;
    flex-direction: column;
    align-items: center;
  }
  .brand {
    margin-top: 120px;
    display: flex;
    flex-direction: column;
    align-items: center;
  }
  .brand__dot {
    width: 150px;
    height: 150px;
    border-radius: 50%;
    background: var(--charcoal);
  }
  .brand__name {
    margin-top: 30px;
    color: var(--ink);
    font-size: 140px;
    font-weight: 700;
    letter-spacing: 6px;
    line-height: 1;
  }
  .phone {
    margin-top: 60px;
    color: var(--ink);
    font-size: 64px;
    font-weight: 400;
    letter-spacing: 2px;
  }
</style>
</head>
<body>
<main class="brochure-cover">
  <section class="hero">
    <svg width="1200" height="1260" viewBox="0 0 1200 1260" xmlns="http://www.w3.org/2000/svg">
      <rect class="hero__backdrop" x="0" y="0" width="1200" height="1260" fill="var(--sand)"/>
      <rect class="hero__figure" role="img" aria-label="Silhouette of a muscular man standing" x="400" y="220" width="440" height="1040" rx="120" fill="var(--figure)"/>
      <polygon class="hero__wedge" points="1200,0 1200,1260 190,1260" fill="var(--charcoal)" fill-opacity="0.96"/>
    </svg>
  </section>

  <section class="title-band">
    <h1 class="title-band__text">Personal Trainer</h1>
  </section>

  <section class="footer-panel">
    <div class="brand">
      <span class="brand__dot"></span>
      <span class="brand__name">VELSTROM</span>
    </div>
    <p class="phone">444-867-3021</p>
  </section>
</main>
</body>
</html>
```